Walt's 85th Birthday Invitation

Invitation to celebrate Walt's turning 85. OKTOBERFEST with fall colors & maybe some beer steins/autumn leaves/happy/fun images. Below are my thoughts for the wording but I need someone to bring it to life.
It's not just a party
it's an
OKTOBERFEST
to celebrate
Picture of Walt
Walt's 85th birthday

Saturday, October 25, 2014

at the Thornwick Ale Yard
Pellorwood
4172 Dunmere Ave.
Hollin Vale, CA 93617

Cocktails at 6 Dinner at 7
Dancing & Partying till 10:00

No birthday gifts please.
Please consider a gift to PellorWood!
Casual Attire

I would like this on a horizontal 5x7 flat card that will fit the envelopes you have. The text & spacing can be adjusted. This is just a rough draft. Thank you for your help! I will need 150 invitations with envelopes.

OktoberFest

```html
<!DOCTYPE html>
<html lang="en">
<head>
<meta charset="utf-8">
<title>Oktoberfest for Walt's 85th</title>
<link rel="stylesheet" href="https://fonts.googleapis.com/css2?family=Montserrat:wght@600;700;800&family=Oswald:wght@400;500;700&display=swap">
<style>
  :root {
    --sky-teal: #3fb4c6;
    --sky-deep: #2e8fb0;
    --mint: #7fd6a6;
    --pale-mist: #b9cdd2;
    --sun-wash: #dedda2;
    --party-red: #c8323f;
    --oktober-red: #c23a40;
    --celebrate-green: #2f6d3a;
    --gold: #f0b420;
    --navy: #1d3a63;
    --white: #ffffff;
    --leaf-orange: #d9531e;
    --tree-green: #6a9a2c;
    --stein-yellow: #e8c41a;
  }
  html, body {
    margin: 0;
    width: 1200px;
    height: 1000px;
    overflow: hidden;
    background: var(--white);
  }
  .invitation {
    position: absolute;
    left: 0;
    top: 78px;
    width: 1200px;
    height: 860px;
    overflow: hidden;
    font-family: "Oswald", "Arial Narrow", sans-serif;
  }
  .backdrop { position: absolute; inset: 0; }
  .tagline {
    position: absolute;
    left: 830px;
    top: 118px;
    margin: 0;
    color: var(--gold);
    font-weight: 700;
    font-size: 56px;
    line-height: 52px;
    text-transform: uppercase;
    transform: rotate(-5deg);
    transform-origin: left top;
    text-shadow: 2px 3px 2px rgba(0,0,0,.35);
  }
  .tagline span { display: block; }
  .tagline span + span { margin-left: 32px; }
  .headline {
    position: absolute;
    left: 40px;
    top: 310px;
    margin: 0;
    font-family: "Montserrat", Arial, sans-serif;
    font-weight: 800;
  }
  .headline .celebrate {
    display: block;
    color: var(--celebrate-green);
    font-weight: 700;
    font-size: 48px;
    line-height: 54px;
    margin-left: 10px;
    letter-spacing: -0.5px;
  }
  .headline .event {
    display: block;
    color: var(--oktober-red);
    font-size: 148px;
    line-height: 120px;
    letter-spacing: -6px;
    text-shadow: 3px 4px 3px rgba(0,0,0,.3);
  }
  .headline .honoree {
    display: block;
    margin-left: 278px;
    font-size: 84px;
    line-height: 96px;
    letter-spacing: -3px;
    text-shadow: 3px 4px 3px rgba(0,0,0,.3);
  }
  .honoree .for { color: var(--gold); }
  .honoree .name { color: var(--navy); }
  .honoree .age { color: var(--oktober-red); }
  .details {
    position: absolute;
    left: 28px;
    top: 652px;
    color: var(--white);
    text-transform: uppercase;
    font-size: 21px;
    line-height: 24px;
    font-weight: 400;
  }
  .details p { margin: 0; }
  .details strong { font-weight: 700; }
  .details .date { font-size: 25px; line-height: 28px; }
  .details .schedule { margin-top: 20px; }
  .details .note {
    margin-top: 30px;
    font-style: italic;
    font-size: 19px;
  }
  .attire {
    position: absolute;
    right: 22px;
    top: 814px;
    margin: 0;
    color: var(--white);
    text-transform: uppercase;
    font-weight: 500;
    font-size: 19px;
  }
</style>
</head>
<body>
<main class="invitation">
  <svg class="backdrop" width="1200" height="860" viewBox="0 0 1200 860">
    <defs>
      <linearGradient id="bunting-tones" x1="0" y1="0" x2="1" y2="0">
        <stop offset="0" stop-color="#b8343c"/>
        <stop offset=".33" stop-color="#f0b420"/>
        <stop offset=".66" stop-color="#237a2e"/>
        <stop offset="1" stop-color="#22348c"/>
      </linearGradient>
      <linearGradient id="mist-band" x1="0" y1="0" x2="1" y2="0">
        <stop offset="0" stop-color="#dedda2"/>
        <stop offset=".5" stop-color="#b9cdd2"/>
        <stop offset="1" stop-color="#a9d6d0"/>
      </linearGradient>
    </defs>
    <!-- sky bands -->
    <rect class="sky" width="1200" height="860" fill="var(--sky-teal)"/>
    <polygon points="0,0 640,0 0,160" fill="#9fd0c4"/>
    <polygon points="0,60 420,0 520,0 0,110" fill="var(--sky-deep)" opacity=".7"/>
    <polygon points="0,170 1200,120 1200,190 0,240" fill="#4fb9c0"/>
    <polygon points="0,240 1200,230 1200,300 0,300" fill="var(--pale-mist)"/>
    <polygon points="0,300 1200,240 1200,380 0,400" fill="var(--mint)"/>
    <polygon points="0,310 1200,330 1200,420 0,470" fill="url(#mist-band)"/>
    <polygon points="0,470 1200,420 1200,470 0,530" fill="#6bc7bf"/>
    <polygon points="0,530 1200,470 1200,640 0,640" fill="#3aa9c0"/>
    <!-- bunting -->
    <polygon role="img" aria-label="String of colourful pennant flags" points="0,154 1185,-8 1160,70 20,230" fill="url(#bunting-tones)" opacity=".85"/>
    <polygon role="img" aria-label="String of colourful pennant flags" points="0,144 1200,300 1200,380 0,230" fill="url(#bunting-tones)" opacity=".85"/>
    <line x1="0" y1="154" x2="1185" y2="-8" stroke="#111" stroke-width="3"/>
    <line x1="0" y1="144" x2="1200" y2="300" stroke="#111" stroke-width="3"/>
    <!-- ground -->
    <polygon class="ground" points="0,612 1200,622 1200,860 0,860" fill="var(--party-red)"/>
    <!-- illustrations -->
    <polygon role="img" aria-label="Autumn leaves illustration" points="0,560 130,515 275,505 300,565 150,600 0,620" fill="var(--leaf-orange)"/>
    <polygon role="img" aria-label="Music note and beer steins illustration" points="1040,400 1150,330 1200,360 1200,670 985,670 985,600 1040,560" fill="var(--stein-yellow)" opacity=".9"/>
    <polygon role="img" aria-label="Stylised geometric tree illustration" points="380,660 560,590 780,560 960,590 1040,700 960,800 800,830 780,860 700,860 560,780 460,740" fill="var(--tree-green)"/>
  </svg>

  <h2 class="tagline"><span>Grab a beer</span><span>Join the party!</span></h2>

  <h1 class="headline">
    <span class="celebrate">Celebrate</span>
    <span class="event">Oktoberfest</span>
    <span class="honoree"><span class="for">for</span><span class="name">Walt’s</span> <span class="age">85th!</span></span>
  </h1>

  <section class="details">
    <p class="date"><strong>Saturday,</strong> October 25, 2014</p>
    <p>Thornwick Ale Yard Pellorwood</p>
    <p>4172 Dunmere Ave. Hollin Vale, CA 93617</p>
    <div class="schedule">
      <p>Cocktails at 6 Dinner at 7</p>
      <p><strong>Dancing and partying till 10</strong></p>
    </div>
    <p class="note">No gifts please - please consider giving to Pellorwood!</p>
  </section>

  <p class="attire">Casual attire only</p>
</main>
</body>
</html>
```